KTR Associates Business Card

I would like to have a business card designed that uses my current logo and colors. I am not looking for anything to "out there" but can have a little fun so that it stands out.

I have a boutique consulting firm that specializes in strategic planning, change management, leadership development and innovation.

Industry/Entity Type

Leadership

Contact Information for Business Card

Marta Holbeck
President
marta@ktr-associates.example
555-014-2286

```html
<!DOCTYPE html>
<html lang="en">
<head>
<meta charset="utf-8">
<title>KTR Associates Business Card</title>
<link rel="stylesheet" href="https://fonts.googleapis.com/css2?family=Lora:wght@400;700&display=swap">
<style>
  :root {
    --page-bg: #ecebe8;
    --card-white: #ffffff;
    --card-black: #2a2a2b;
    --ink: #1d1d1d;
    --ink-soft: #4a4a4a;
    --green-deep: #3f8f2e;
    --green-mid: #6fae34;
    --green-light: #a9cf4a;
    --rule: #2b2b2b;
  }
  * { margin: 0; padding: 0; box-sizing: border-box; }
  html, body {
    width: 1200px;
    height: 900px;
    overflow: hidden;
    background: var(--page-bg);
    font-family: "Lora", Georgia, serif;
    color: var(--ink);
  }
  .sheet {
    position: relative;
    width: 1200px;
    height: 900px;
    display: flex;
    flex-direction: column;
    align-items: center;
    justify-content: center;
    gap: 60px;
  }
  .card {
    position: relative;
    width: 640px;
    height: 366px;
    border-radius: 4px;
    overflow: hidden;
    box-shadow: 0 6px 18px rgba(0, 0, 0, 0.18);
  }

  /* Front */
  .card-front { background: var(--card-white); }
  .brush-band {
    position: absolute;
    opacity: 0.85;
    border-radius: 40px;
  }
  .brush-band-top {
    left: 150px;
    top: 18px;
    width: 470px;
    height: 100px;
    background: linear-gradient(100deg, var(--green-deep) 0%, var(--green-mid) 45%, var(--green-light) 100%);
    transform: rotate(6deg);
    opacity: 0.55;
  }
  .brush-band-bottom {
    left: 40px;
    top: 226px;
    width: 520px;
    height: 80px;
    background: linear-gradient(100deg, var(--green-deep) 0%, var(--green-mid) 50%, var(--green-light) 100%);
    transform: rotate(6deg);
    opacity: 0.5;
  }
  .email {
    position: absolute;
    left: 34px;
    top: 30px;
    font-size: 14px;
    font-weight: 700;
    color: var(--ink);
  }
  .identity {
    position: absolute;
    left: 0;
    right: 0;
    top: 150px;
    display: flex;
    justify-content: center;
    align-items: center;
    gap: 18px;
  }
  .wordmark {
    display: flex;
    align-items: center;
    gap: 8px;
    font-size: 26px;
    font-weight: 400;
    color: var(--ink);
  }
  .wordmark-square {
    width: 12px;
    height: 12px;
    background: var(--green-deep);
  }
  .divider {
    width: 1.5px;
    height: 64px;
    background: var(--rule);
  }
  .person-name {
    font-size: 22px;
    font-weight: 700;
    line-height: 1.1;
  }
  .person-name .surname { color: var(--green-deep); }
  .person-title {
    font-size: 14px;
    color: var(--ink-soft);
    margin-top: 2px;
  }
  .phone {
    position: absolute;
    right: 34px;
    bottom: 26px;
    font-size: 14px;
    font-weight: 700;
  }

  /* Back */
  .card-back {
    background: var(--card-black);
  }
  .gloss {
    position: absolute;
    inset: 0;
    background: linear-gradient(152deg, rgba(255,255,255,0.16) 0%, rgba(255,255,255,0.06) 40%, rgba(255,255,255,0) 41%);
  }
</style>
</head>
<body>
  <main class="sheet">
    <section class="card card-front" aria-label="Business card front">
      <div class="brush-band brush-band-top" role="img" aria-label="Green painted brush stroke texture"></div>
      <div class="brush-band brush-band-bottom" role="img" aria-label="Green painted brush stroke texture"></div>
      <p class="email">marta@ktr-associates.example</p>
      <div class="identity">
        <div class="wordmark">
          <span class="wordmark-square" aria-hidden="true"></span>
          <span class="wordmark-name">KTR Associates</span>
        </div>
        <span class="divider" aria-hidden="true"></span>
        <div class="person">
          <p class="person-name">Marta <span class="surname">Holbeck</span></p>
          <p class="person-title">President</p>
        </div>
      </div>
      <p class="phone">555-014-2286</p>
    </section>

    <section class="card card-back" aria-label="Business card back">
      <div class="gloss" aria-hidden="true"></div>
    </section>
  </main>
</body>
</html>
```